1 page A4 double sided Brochure Design Folded to envelope size. Interesting fold design would be co

Small family run guesthouse BnB in Blue Mountains Australia needs a new brochure showing different aspects of business

We need a new brochure to go with our new website. Basically the design would be good as a double sided brochure that can be folded down to standard envelope size.

We have seen a few interesting brochure designs before that fold in different ways (and therefore have the design to match) but still fold down to this size to help with postage.

The design would have to showcase the different aspects of our business including individual accommodation for couples and families, conference market, wedding market, retreat market and events market (parties, re-unions etc). The Business must be Showcased as The Fernhollow Lodge, Blue Mountains

It is possible to arrange design so folds separate different sections of info/pictures.

It is also optional that we possibly have 2 brochures instead, one that is a basic all inclusive once described and one that only deals with group bookings (wedding conference retreats etc etc)

Must match design elements from our web page. Feel free to take informations, elements and images from there for design www.fernhollowlodge.com.au

Here is a link to our view we wake up to every morning to inspire all those working on a design!
http://www.fernhollowlodge.com.au/images/view.jpg

Target Market(s)

Group bookings, weddings, conferences, retreats, events and Blue Mountains Travellers

Industry/Entity Type

Accommodation

Requirements
Must have
• Must be based on our current websites design feel, colours, etc
Must be showcased as The Fernhollow Lodge Blue Mountains.
Must mention The Blue Mountains as a world heritage destination
Must be A4 double sided that can fold down to 1/3 the size to fit into a standard envelope. Any designs that will not fit in a standard envelope once folded can not be accepted as they are outside the brief
Nice to have
• Interesting folding design to get people interested to read it.

```html
<!DOCTYPE html>
<html lang="en">
<head>
<meta charset="utf-8">
<title>The Fernhollow Lodge – Brochure</title>
<link href="https://fonts.googleapis.com/css2?family=Crimson+Text:ital,wght@0,400;0,600;0,700;1,600;1,700&family=Allura&family=Kaushan+Script&family=Istok+Web:wght@400;700&family=Roboto:wght@400;700&display=swap" rel="stylesheet">
<style>
:root{
  --backdrop:#a67c53;
  --paper:#ffffff;
  --bark:#3b372f;
  --cream:#e8eecb;
  --sage:#dfeacc;
  --sage-light:#e4eed6;
  --ink:#2d2a25;
  --muted:#d9d4c6;
  --rule:#cfc9b8;
}
*{margin:0;padding:0;box-sizing:border-box}
html,body{width:1200px;height:1000px;overflow:hidden;background:var(--backdrop)}
.brochure{position:absolute;left:302px;top:80px;width:595px;height:840px;background:var(--paper);font-family:"Crimson Text",Georgia,serif;color:var(--ink);box-shadow:0 2px 8px rgba(0,0,0,.35)}
.hero-photo{position:absolute;left:9px;top:8px;width:280px;height:92px;background:linear-gradient(180deg,#9fb7cf 0%,#6e8a5a 45%,#3f8fb0 75%,#5b6a48 100%)}
.hero-title{position:absolute;left:289px;top:8px;width:297px;height:92px;background:var(--bark);display:flex;align-items:center;justify-content:center}
.hero-title h1{font-family:"Allura",cursive;font-weight:400;font-size:44px;color:var(--cream);border-bottom:1px solid var(--cream);line-height:1;padding:0 4px 2px}
.intro{position:absolute;left:9px;top:114px;width:282px;font-size:9.2px;line-height:1.35;text-align:justify}
.intro p{margin-bottom:7px}
.intro .url{text-align:center;color:#e4e8c8;letter-spacing:1.5px;font-size:8px;margin-top:6px}
.rooms{position:absolute;left:303px;top:117px;width:284px}
.room{position:relative;height:38px;font-size:6.2px;line-height:1.3}
.room .thumb{position:absolute;top:0;width:82px;height:30px}
.room.left .thumb{left:0}
.room.right .thumb{right:0}
.room .text{position:absolute;top:2px;width:198px}
.room.left .text{left:86px}
.room.right .text{left:0;text-align:right}
.room h3{font-family:"Allura",cursive;font-weight:400;font-size:11px;line-height:1}
.services{position:absolute;left:0;top:280px;width:595px;height:281px;background:var(--bark);color:var(--muted);font-size:5.7px;line-height:1.65}
.services .heading{position:absolute;font-style:italic;font-weight:700;font-size:11px;color:var(--cream);display:flex;align-items:center;gap:8px;line-height:1}
.services .heading::after{content:"";flex:1;height:1px;background:var(--rule)}
.services .block{position:absolute;text-align:justify}
.services .block p{margin-bottom:7px}
.services-badge{position:absolute;left:196px;top:112px;width:202px;height:55px;background:var(--sage);display:flex;align-items:center;justify-content:center}
.services-badge h2{font-family:"Kaushan Script",cursive;font-weight:400;font-size:30px;color:var(--bark)}
.map{position:absolute;left:0;top:561px;width:595px;height:177px;background:linear-gradient(90deg,#e9e5dc 0%,#ece8e0 45%,#cfe0b3 70%,#c8dcab 100%)}
.map-card{position:absolute;left:255px;top:37px;width:146px;height:77px;background:#f3f7ee;border:1px solid #c9cfc2;font-family:"Roboto",Arial,sans-serif;font-size:7.5px;line-height:1.55;padding:5px 8px;color:#333}
.map-card strong{display:flex;justify-content:space-between;margin-bottom:5px}
.map-card strong span{font-weight:400}
.map-pin{position:absolute;left:320px;top:125px}
.directions{position:absolute;left:0;top:738px;width:595px;height:102px;background:var(--sage-light);font-family:"Istok Web",Arial,sans-serif;font-size:7.4px;line-height:1.6;color:#3a3a32;padding:7px 9px 0}
.directions p{margin-bottom:5px}
</style>
</head>
<body>
<main class="brochure">
  <div class="hero-photo" role="img" aria-label="Photo of the lodge pool terrace with umbrellas and bushland"></div>
  <div class="hero-title"><h1>The Property</h1></div>

  <section class="intro">
    <p><strong>The Fernhollow Lodge</strong> sits on 32 acres of virgin bushland affording guests some of the most spectacular views, Native Bush, rain forest, waterfall, flora, fauna and birdlife the Blue Mountains has on offer.</p>
    <p>Take in the peace and serenity with fellow guests or your own private group while experiencing a world like no other.</p>
    <p>There is even a small private bush walk from the property down the valley into Fern Glen Dell to your own private waterfall experience.</p>
    <p>All just 100km from Sydney and only 900metres to Wentworth Falls village it wont take long to realise.</p>
    <p class="url">www.fernhollowlodge.com.au</p>
  </section>

  <section class="rooms">
    <div class="room left"><div class="thumb" role="img" aria-label="Photo of a retreat bedroom" style="background:linear-gradient(90deg,#6b4a33,#b9a58a)"></div>
      <div class="text"><h3>The Retreat Rooms</h3>Each wing in the retreat is also dedicated to another great mind and is lightly decorated to match their theme.</div></div>
    <div class="room right"><div class="thumb" role="img" aria-label="Photo of a function room set with tables" style="background:linear-gradient(90deg,#8a6a4c,#3c4a5c)"></div>
      <div class="text"><h3>The Function Rooms</h3>With a range of different areas and function rooms we can help with any kind of event in the Blue Mountains.</div></div>
    <div class="room left"><div class="thumb" role="img" aria-label="Photo of the manor lounge" style="background:linear-gradient(90deg,#c49a4a,#7a5a36)"></div>
      <div class="text"><h3>The Fernhollow Manor</h3>Sleeping over 20 people The Manor is the perfect place to base your family or group for a Blue Mountains adventure.</div></div>
    <div class="room right"><div class="thumb" role="img" aria-label="Photo of a yellow guest bedroom" style="background:linear-gradient(90deg,#d8b236,#e9e2cf)"></div>
      <div class="text"><h3>View On Larkin</h3>View On Larkin is a perfect private place to based your small group for a Blue Mountains escape. Please visit www.viewonlarkin.com.au</div></div>
  </section>

  <section class="services">
    <h2 class="heading" style="left:9px;top:10px;width:280px">Conferences</h2>
    <div class="block" style="left:9px;top:29px;width:280px">
      <p>With our experienced professional team we can also privately cater meals for groups of 10 or more attendees with our own special style of hearty mountains buffet style catering. No muss, no fuss, just let us know your numbers and special dietary needs and we do the rest. We are also fully licensed with Australian beer on tap and a great selection of local wines.</p>
      <p>With a great friendly support staff and a full time interpretive guide we can help you plan your full event whether a small discrete board meeting or a large corporate event.</p>
      <p style="width:178px">Contact us today to discuss our special exclusive use packages so you can plan the perfect, private conference and help your organization achieve all its most important goals.</p>
    </div>

    <h2 class="heading" style="left:303px;top:10px;width:283px">Weddings</h2>
    <div class="block" style="left:303px;top:29px;width:284px">
      <p>The Fernhollow Lodge is the perfect, private, flexible venue for your special day.</p>
      <p>At The Fernhollow Lodge you can have your ceremony, reception and accommodation for all your guests for the price you normally pay for one and get all 3. With accommodation for up to 70 people we can help you plan your wedding your way. Whether its a cocktail style wedding for 150 people, a formal sit down reception for 70, or a quiet, casual picnic basket event for 40 we have seen it all at The Fernhollow Lodge.</p>
      <p>Every event at The Fernhollow Lodge is completely different so get in contact and make an appointment <span style="display:block;padding-left:107px">today so we can show you around the property and start helping you organize everything to your own personality.</span></p>
    </div>

    <div class="services-badge"><h2>Our Services</h2></div>

    <h2 class="heading" style="left:9px;top:146px;width:178px">Retreat</h2>
    <div class="block" style="left:9px;top:165px;width:280px">
      <p><span style="display:block;width:178px">At The Fernhollow Lodge we have all these strengths and more. We have become the perfect choice for your</span>next Blue Mountains retreat whether it be spiritual, religious, physical, mental, relating or more.</p>
      <p>With extensive experience in facilitating a wide range of alternate beliefs and mindsets our quirky, inspiring venue, originally decorated and dedicated to the great minds of the world will unlock your groups absolute potential.</p>
      <p>With the ability to take the whole retreat exclusively where we can cater or you can self cater and manage our flexibility allows you to tailor your packge to your own personal needs. All at a great discount rate for group bookings.</p>
    </div>

    <h2 class="heading" style="left:410px;top:146px;width:176px">Events</h2>
    <div class="block" style="left:303px;top:165px;width:284px">
      <p><span style="display:block;padding-left:107px">Reunions, birthdays, church groups, parties, family get</span>togethers and more The Fernhollow Lodge Blue Mountains is the perfect function venue to get together and really leave the world behind whilst re-connecting with your friends and family.</p>
      <p>At The Fernhollow Lodge we can cater for any type of function or event or recommend the perfect caterer to suit your needs and budget. We are also fully licensed with Australian beer on tap and an excellent selection of local wines so can cover all your beverage needs as well.</p>
      <p>Once you take The Fernhollow Lodge exclusively it becomes your own private haven from the rest of civilization to really break free and re-establish the truely important things.</p>
    </div>
  </section>

  <section class="map" role="img" aria-label="Street map of Wentworth Falls showing the lodge location near the highway">
    <div class="map-card">
      <strong>The Fernhollow Lodge <span>$180</span></strong>
      18-22 Ridgeview Parade<br>
      Wentworth Falls NSW 2782<br>
      (02) 4710 5583<br>
      fernhollowlodge.com.au
    </div>
    <svg class="map-pin" width="20" height="28" viewBox="0 0 20 28" aria-hidden="true">
      <path d="M10 1C5 1 1.5 4.6 1.5 9.2 1.5 15 10 27 10 27s8.5-12 8.5-17.8C18.5 4.6 15 1 10 1z" fill="#e8625a" stroke="#a33a33" stroke-width="1"/>
      <circle cx="10" cy="9" r="3" fill="#8f2c26"/>
    </svg>
  </section>

  <section class="directions">
    <p>If coming from Sydney travel along the M4 into the Great Western Highway into the Blue Mountains. Stay on the Great Western Highway all the way to Wentworth Falls Village. Turn Right at the lights into the village shops at Station Street. At the end of the village shopping area go over the small bridge over the railway line.</p>
    <p>As soon as you come off the bridge take the very sharp right hand turn back into Ridgeview parade. Travel along Ridgeview parade about 1km to find The Fernhollow Lodge on the left hand side. Our main gates have our name on them in very large print.</p>
    <p>For those travelling from the west the directions are the same except you will need to turn left into Station street off the Great Western Highway.</p>
    <p>Please call us on <strong>02 4710 5583</strong> any time if you are having any trouble finding The Fernhollow Lodge.</p>
  </section>
</main>
</body>
</html>
```